my company buys cars,boats and caravans off the public, and also assists the public in helping them sell there item(brokering),i have an idea of a logo which is.....T$D....THE S BEING A LARGE DOLLAR SIGN,centred. And underneath my business name....TRADER-HAULER-DEALER,i like black backgrounds, CLEAN SHARP AND TO THE POINT!!

Industry/Entity Type

Business

Contact Information for Business Card

$wap NOW.........buyer,seller,broker......cars,boats,caravans...........0427596041.......-swapnow@traderhaulerdealer.com.au, lmct-47815

Requirements
Must have
• MOBILE NUMBER-0427596041
EMAIL-swapnow@traderhaulerdealer.com.au
business name-TRADER-HAULER-DEALER
lmct-47815
what we deal in-Cars,Caravans,Boats
cash,bank chq, finance paid out
Nice to have
• clever logo created by you guys

```html
<!DOCTYPE html>
<html lang="en">
<head>
<meta charset="utf-8">
<title>Trader-Hauler-Dealer — Business Card</title>
<link rel="stylesheet" href="https://fonts.googleapis.com/css2?family=Poiret+One&family=Questrial&display=swap">
<style>
  :root {
    --backdrop: #9a9b9d;
    --backdrop-light: #b4b5b7;
    --card-paper: #f7f7f5;
    --ink: #1c1c1c;
    --rule: #2a2a2a;
    --card-shadow: rgba(0, 0, 0, 0.28);
  }

  html, body {
    margin: 0;
    padding: 0;
    width: 1200px;
    height: 750px;
    overflow: hidden;
  }

  .canvas {
    position: relative;
    width: 1200px;
    height: 750px;
    background: radial-gradient(ellipse at 50% 40%, var(--backdrop-light), var(--backdrop));
    display: flex;
    align-items: center;
    justify-content: center;
  }

  .business-card {
    position: relative;
    width: 840px;
    height: 480px;
    background: var(--card-paper);
    box-shadow: 0 18px 40px var(--card-shadow);
    color: var(--ink);
    font-family: "Questrial", "Century Gothic", sans-serif;
  }

  .brand {
    position: absolute;
    left: 180px;
    top: 120px;
    width: 380px;
    text-align: center;
  }

  .brand-name {
    margin: 0;
    font-family: "Poiret One", "Century Gothic", sans-serif;
    font-weight: 400;
    font-size: 40px;
    letter-spacing: 0.5px;
    line-height: 1;
  }

  .brand-rule {
    display: block;
    margin: 14px auto 0;
  }

  .offer {
    position: absolute;
    left: 150px;
    top: 205px;
    width: 440px;
    text-align: center;
    font-size: 17px;
    letter-spacing: 0.4px;
    line-height: 1;
  }

  .offer p {
    margin: 0 0 22px;
  }

  .contact {
    position: absolute;
    right: 70px;
    top: 300px;
    text-align: right;
    font-size: 22px;
    line-height: 1.3;
  }

  .contact p {
    margin: 0;
  }
</style>
</head>
<body>
  <main class="canvas">
    <section class="business-card" aria-label="Trader-Hauler-Dealer business card">
      <header class="brand">
        <h1 class="brand-name">Trader-Hauler-Dealer</h1>
        <svg class="brand-rule" width="330" height="3" viewBox="0 0 330 3" aria-hidden="true">
          <line x1="0" y1="1.5" x2="330" y2="1.5" stroke="var(--rule)" stroke-width="2"/>
        </svg>
      </header>

      <div class="offer">
        <p class="offer-goods">CARS,CARAVANS,BOATS</p>
        <p class="offer-payment">CASH,BANK CHQ, FINANCE PAID OUT</p>
      </div>

      <address class="contact" style="font-style: normal;">
        <p class="contact-licence">LMCT:- 47815</p>
        <p class="contact-phone">0427596041</p>
        <p class="contact-email">swapnow@traderhaulerdealer.com.au</p>
      </address>
    </section>
  </main>
</body>
</html>
```